Brivenor Australia Company Values.

We have just completed our company purpose, beliefs and values (for the first time, we have not had these before)
We are now wanting to add images to each company value as a visual
so they are easily identified and understood for all our staff - we need them to remember the 5 Values.
We are a manufacturer of dental materials and infection control products, based in Melbourne.

What we would like:
- A Poster (that can be placed in our staff lunch rooms)
- The values to be lined up Horizontally
- Image on the top of the words
- Wording does not all need to be the same text font
- No image photographs - please use image graphics
- No images with people
- No dental related graphics

Target audience: Brivenor staff

Our Values are:
Think Big
Have a go, learn and adapt
If you're gonna do it, do it bloody well
Empower Others
Be a good human

I have uploaded some examples.

Target Market(s)

Brivenor Team members

Industry/Entity Type

Healthcare

Colors

Designer to choose colors to be used in the design.

Requirements
Must have
• Clear horizontal layout, space between each value
Should not have
• No images with humans or dental

```html
<!DOCTYPE html>
<html lang="en">
<head>
<meta charset="utf-8">
<title>Brivenor Australia – Company Values</title>
<link rel="stylesheet" href="https://fonts.googleapis.com/css2?family=Barlow:wght@700;800&display=swap">
<style>
  :root {
    --page: #ffffff;
    --band: #41b845;
    --ink: #18285c;
    --line: #ffffff;
    --icon-fill: rgba(255, 255, 255, 0.85);
  }
  html, body {
    margin: 0;
    padding: 0;
    width: 1200px;
    height: 549px;
    overflow: hidden;
    background: var(--page);
  }
  .poster {
    position: relative;
    width: 1200px;
    height: 549px;
    font-family: "Barlow", Arial, sans-serif;
    font-weight: 800;
    color: var(--ink);
  }
  .values-band {
    position: absolute;
    left: 106px;
    top: 177px;
    width: 989px;
    height: 194px;
    background: var(--band);
  }
  .divider {
    position: absolute;
    top: 235px;
    height: 92px;
    border-left: 1px dashed var(--line);
  }
  .value-icon {
    position: absolute;
    top: 201px;
    width: 60px;
    height: 60px;
    border-radius: 12px;
    background: var(--icon-fill);
  }
  .value-icon.wide { width: 74px; }
  .line {
    position: absolute;
    line-height: 1;
    white-space: nowrap;
    letter-spacing: -0.02em;
  }
  .centered { transform: translateX(-50%); }
  .xs { font-size: 14px; font-weight: 700; letter-spacing: 0; }
  .sm { font-size: 17px; font-weight: 700; letter-spacing: -0.01em; }
  .md { font-size: 22px; }
  .lg { font-size: 36px; }
  .xl { font-size: 42px; }
  .xxl { font-size: 62px; }
</style>
</head>
<body>
<main class="poster">
  <section class="values-band" aria-label="Company values"></section>

  <span class="divider" style="left:257px"></span>
  <span class="divider" style="left:426px"></span>
  <span class="divider" style="left:682px"></span>
  <span class="divider" style="left:890px"></span>

  <div class="value-icon" style="left:161px" role="img" aria-label="Brain icon with spark lines"></div>
  <div class="value-icon" style="left:310px" role="img" aria-label="Reader holding an open book icon"></div>
  <div class="value-icon wide" style="left:497px" role="img" aria-label="Two figures high-fiving icon"></div>
  <div class="value-icon" style="left:758px" role="img" aria-label="Raised fist icon"></div>
  <div class="value-icon" style="left:954px" role="img" aria-label="Thumbs up icon"></div>

  <span class="line md centered" style="left:189px;top:273px">Think</span>
  <span class="line xxl centered" style="left:191px;top:287px">BIG</span>

  <span class="line xs" style="left:300px;top:273.5px">HAVE A GO,</span>
  <span class="line lg" style="left:273px;top:278.5px">Learn &amp;</span>
  <span class="line lg" style="left:289px;top:309.5px">Adapt</span>

  <span class="line sm" style="left:451px;top:273px">IF YOU'RE</span>
  <span class="line sm" style="left:451px;top:289px">GONNA DO IT</span>
  <span class="line xl" style="left:565px;top:268.5px">Do It</span>
  <span class="line xl" style="left:443px;top:304.5px">Bloody Well</span>

  <span class="line xl" style="left:701px;top:267px">Empower</span>
  <span class="line xl" style="left:726px;top:305px">Others</span>

  <span class="line sm" style="left:908px;top:288px;font-size:18px">BE A</span>
  <span class="line xl" style="left:958px;top:266.5px">good</span>
  <span class="line xl" style="left:917px;top:304.5px">human</span>
</main>
</body>
</html>
```